Pain cream backed by Pro-Athletes "Glacier Ember"

Looking to revamp the label brand.
It's an all-natural pain gel. It heats then cools. Looking for a very sharp look that gets the point of the product use across.
Eveyrthing about the original label can be changed except for the text. It still needs to have the same information but can be any color, font whatever.,
I'll need pdf's and ai files of the design.
Label Size die line is attached.
Original Label is attached.

```html
<!DOCTYPE html>
<html lang="en">
<head>
<meta charset="utf-8">
<title>Glacier Ember – Label</title>
<link rel="stylesheet" href="https://fonts.googleapis.com/css2?family=Montserrat:wght@600;800&family=Oswald:wght@500&display=swap">
<style>
  :root {
    --page: #ffffff;
    --ice-light: #e3edf1;
    --ice-mid: #c9dde5;
    --ice-deep: #b3cdd8;
    --navy: #272d4f;
    --teal: #3ba4c3;
    --slate: #6d7075;
  }
  html, body {
    margin: 0;
    padding: 0;
    width: 1200px;
    height: 1200px;
    overflow: hidden;
    background: var(--page);
  }
  .canvas {
    position: relative;
    width: 1200px;
    height: 1200px;
  }
  .label {
    position: absolute;
    left: 380px;
    top: 100px;
    width: 440px;
    height: 1000px;
    overflow: hidden;
  }
  .label-texture {
    position: absolute;
    inset: 0;
    width: 100%;
    height: 100%;
  }
  .label-copy {
    position: absolute;
    width: 1000px;
    height: 440px;
    left: -280px;
    top: 280px;
    transform: rotate(-90deg);
  }
  .product-name {
    position: absolute;
    left: 110px;
    top: 150px;
    margin: 0;
    font-family: "Montserrat", sans-serif;
    font-weight: 800;
    font-size: 88px;
    line-height: 1;
    letter-spacing: 1px;
    white-space: nowrap;
    color: var(--navy);
  }
  .product-name .accent {
    color: var(--teal);
  }
  .tagline {
    position: absolute;
    left: 114px;
    top: 290px;
    margin: 0;
    font-family: "Montserrat", sans-serif;
    font-weight: 600;
    font-size: 26px;
    line-height: 1;
    letter-spacing: 17px;
    white-space: nowrap;
    color: var(--slate);
  }
  .volume {
    position: absolute;
    left: 740px;
    top: 284px;
    margin: 0;
    font-family: "Oswald", sans-serif;
    font-weight: 500;
    font-size: 30px;
    line-height: 1;
    white-space: nowrap;
    color: var(--navy);
  }
</style>
</head>
<body>
  <main class="canvas">
    <section class="label">
      <svg class="label-texture" viewBox="0 0 440 1000" preserveAspectRatio="none" role="img" aria-label="Frosted ice crystal texture in pale blue tones">
        <defs>
          <linearGradient id="ice" x1="0" y1="0" x2="1" y2="1">
            <stop offset="0" stop-color="#b3cdd8"/>
            <stop offset="0.45" stop-color="#e3edf1"/>
            <stop offset="1" stop-color="#c9dde5"/>
          </linearGradient>
        </defs>
        <rect width="440" height="1000" fill="url(#ice)"/>
      </svg>
      <div class="label-copy">
        <h1 class="product-name">GLACIER <span class="accent">EMBER</span></h1>
        <p class="tagline">GETS YOU BACK UP</p>
        <p class="volume">100ml (3.2oz)</p>
      </div>
    </section>
  </main>
</body>
</html>
```